Australian training business needs a flyer design it will use to promote its collaboration skills tr

We need a flyer that will promote our collaboration skills training short course. My business runs a series of short courses for corporate clients, such as presentation skills training and communications training. The flyer will most likely be sent to potential clients as a PDF, though it may also be printed, so I would like something that can be read on one page. It needs to excite them about training with us, this training is highly relevant for businesses building new teams and wanting people to work together well on projects. The training is also fun, so even though it's a corporate market they have a desire to be more creative and collaborative like the "creative industries", but they don't know how. Many of our clients work in the construction, industrial services and health industries - quite diverse. We want to make them think that this is the best 2.5 hours they could possibly spend.

Tandem Speakworks is the business name and I would like to see colours that reflect the logo, but I am not wedded to that. I suggest using the photo of Moira Calvetti (the trainer) small, if at all. If you use any stock photos I would prefer to see a mix of professional men and women working together, though I am not wedded to using stock imagery..industrial/technical feel with a creative flair might work.

Target Market(s)

Professional Business executives, ages 30 - 55

Industry/Entity Type

Training

Font styles to use
Sans Serif

Requirements
Must have
• Tandem Speakworks logo
• Course detail
• A Call to action:
• "Call or email Tandem Speakworks today to ask about our special course rate for existing clients"
Nice to have
• A look that appeals to the professions.
• Could include the price, I am undecided on this.
Should not have
• Bad American looking stock photos as we are an Australian company

```html
<!DOCTYPE html>
<html lang="en">
<head>
<meta charset="utf-8">
<title>Collaboration Skills Short Course – Tandem Speakworks</title>
<link href="https://fonts.googleapis.com/css2?family=Open+Sans:ital,wght@0,400;0,600;0,700;0,800;1,400;1,600&display=swap" rel="stylesheet">
<style>
  :root{
    --teal:#1f9bb5;
    --teal-dark:#16798e;
    --lime:#9cc31c;
    --ink:#2b3338;
    --grey:#5d666b;
    --footer:#3e4a50;
    --paper:#ffffff;
  }
  *{margin:0;padding:0;box-sizing:border-box}
  html,body{width:900px;height:1200px;overflow:hidden;background:#e9e9e9}
  body{font-family:"Open Sans",Arial,sans-serif;color:var(--ink)}
  .flyer{position:relative;width:900px;height:1200px;background:var(--paper);overflow:hidden}
  .top-band{position:absolute;left:0;top:0;width:900px;height:14px;background:linear-gradient(90deg,var(--teal),var(--lime))}

  .brand{position:absolute;left:44px;top:46px;display:flex;align-items:center;gap:14px}
  .brand-dot{width:62px;height:62px;border-radius:50%;background:var(--teal)}
  .brand-name{font-weight:700;font-size:24px;color:var(--teal);line-height:1.1;letter-spacing:.5px}

  .headline{position:absolute;left:392px;top:28px;width:480px}
  .headline .h1{font-size:58px;font-weight:800;color:var(--teal);line-height:1}
  .headline .h2{font-size:124px;font-weight:800;color:var(--lime);line-height:.95;letter-spacing:-2px}
  .headline .h3{font-size:31px;font-weight:700;color:var(--ink);line-height:1.1;margin-top:2px;white-space:nowrap}

  .intro{position:absolute;left:44px;top:190px;width:320px;font-size:15.5px;font-weight:700;line-height:1.45;color:var(--ink)}

  .hero{position:absolute;left:400px;top:258px}

  .badge{position:absolute;left:190px;top:440px;width:180px;height:180px;border-radius:50%;background:var(--teal);
    display:flex;align-items:center;justify-content:center;text-align:center;color:#fff;font-weight:800;font-size:19px;line-height:1.2;
    border:5px solid #fff;box-shadow:0 0 0 4px var(--lime)}

  .team-title{position:absolute;left:44px;top:636px;font-size:25px;font-weight:800;color:var(--ink);line-height:1.15}
  .benefits{position:absolute;left:44px;top:708px;width:370px;list-style:none}
  .benefits li{display:flex;gap:14px;align-items:flex-start;margin-bottom:12px;font-style:italic;font-weight:600;font-size:16px;line-height:1.35;color:var(--teal-dark)}
  .benefits .num{flex:0 0 30px;height:30px;border-radius:50%;background:var(--teal);color:#fff;font-style:normal;font-weight:700;font-size:15px;display:flex;align-items:center;justify-content:center;margin-top:2px}

  .summary{position:absolute;left:44px;top:992px;width:380px;font-size:16px;font-weight:700;line-height:1.4;color:var(--teal-dark)}

  .trainer{position:absolute;left:470px;top:710px;width:255px;text-align:right;font-size:14px;line-height:1.4;color:var(--ink)}
  .trainer strong{display:block;font-size:16px;color:var(--ink)}
  .trainer-photo{position:absolute;left:745px;top:694px;width:115px;height:115px;border-radius:50%;
    background:radial-gradient(circle at 50% 40%,#e8c7a8,#b98a64 60%,#8a5e3f);border:5px solid var(--lime)}

  .about{position:absolute;left:470px;top:822px;width:390px;font-size:14px;line-height:1.5;color:var(--grey)}
  .about p+p{margin-top:10px}
  .cta{position:absolute;left:470px;top:1040px;width:390px;font-size:14.5px;font-weight:700;line-height:1.4;color:var(--lime)}

  .footer{position:absolute;left:0;top:1100px;width:900px;height:100px;background:var(--footer);border-top:8px solid var(--lime);color:#fff;display:flex;align-items:center;padding:0 40px;gap:40px}
  .footer .more{width:260px}
  .footer .more b{display:block;font-size:22px;font-weight:800}
  .footer .more span{font-size:15px}
  .contact{display:flex;flex-direction:column;gap:10px;font-size:17px;font-weight:600}
  .contact div{display:flex;align-items:center;gap:10px}
  .icon{width:24px;height:24px;border-radius:50%;background:var(--lime);display:flex;align-items:center;justify-content:center}
</style>
</head>
<body>
<div class="flyer">
  <div class="top-band"></div>

  <div class="brand">
    <div class="brand-dot"></div>
    <div class="brand-name">Tandem<br>Speakworks</div>
  </div>

  <div class="headline">
    <div class="h1">Collaboration</div>
    <div class="h2">SKILLS</div>
    <div class="h3">SHORT COURSE (2.5 HOURS)</div>
  </div>

  <p class="intro">The Collaboration Skills course improves participants' ability to work together creatively as a team. It provides two processes that participants can use anytime, anywhere to work through a challenge. This workshop has a strong practical component and we recommend that the group brings a single real-world challenge to the course to work on.</p>

  <svg class="hero" width="490" height="430" viewBox="0 0 490 430">
    <defs>
      <linearGradient id="heroFill" x1="0" y1="0" x2="1" y2="1">
        <stop offset="0" stop-color="#d9e4ea"/>
        <stop offset=".5" stop-color="#b7c6cf"/>
        <stop offset="1" stop-color="#8ea3ad"/>
      </linearGradient>
    </defs>
    <path d="M290 14 A203 203 0 1 1 60 250" fill="none" stroke="var(--lime)" stroke-width="14"/>
    <path d="M72 140 A203 203 0 0 1 190 28" fill="none" stroke="var(--teal)" stroke-width="8"/>
    <circle cx="262" cy="215" r="182" fill="url(#heroFill)" role="img" aria-label="Photo of professional men and women collaborating around a table with a laptop"/>
  </svg>

  <div class="badge">BRING A<br>REAL-WORLD<br>CHALLENGE<br>TO THE TABLE</div>

  <div class="team-title">YOUR<br>TEAM WILL...</div>
  <ol class="benefits">
    <li><span class="num">1</span>Discover the personal behaviour needed for successful collaboration to take place</li>
    <li><span class="num">2</span>Learn practical skills from positive body language to listening with empathy</li>
    <li><span class="num">3</span>Move away from the silo mentality and build trust</li>
    <li><span class="num">4</span>Learn how to build a successful collaborative team from the ground up</li>
    <li><span class="num">5</span>Learn a 5 step collaborative process for problem solving</li>
  </ol>

  <p class="summary">The Collaboration Skills Short Course is a 2.5 hour course for up to 8 people, at your premises.</p>

  <div class="trainer"><strong>Moira Calvetti</strong>Principal, Tandem Speakworks<br>Managing Director,<br>Tandem Speakworks</div>
  <div class="trainer-photo" role="img" aria-label="Portrait photo of trainer Moira Calvetti"></div>

  <div class="about">
    <p>I've been helping executives to look, act and sound like leaders for the past eight years, working with people in a variety of industries to ensure that their messages are crafted into persuasive presentations.</p>
    <p>Knowledge hoarding and the silo mentality of many in large organisations led me to develop courses to help people in business communicate and collaborate more effectively. I bring my small business creativity and communications experience to companies that are struggling to work together creatively.</p>
  </div>
  <p class="cta">Call or email Tandem Speakworks today to ask about our special course rate for existing clients.</p>

  <div class="footer">
    <div class="more"><b>For more information</b><span>Moira Calvetti, Principal</span></div>
    <div class="contact">
      <div><span class="icon"><svg width="14" height="14" viewBox="0 0 24 24"><path fill="#fff" d="M6.6 10.8a15 15 0 0 0 6.6 6.6l2.2-2.2a1 1 0 0 1 1-.25 11.4 11.4 0 0 0 3.6.57 1 1 0 0 1 1 1V20a1 1 0 0 1-1 1A17 17 0 0 1 3 4a1 1 0 0 1 1-1h3.5a1 1 0 0 1 1 1c0 1.25.2 2.45.57 3.57a1 1 0 0 1-.25 1z"/></svg></span>(08) 5550 1420</div>
      <div><span class="icon"><svg width="14" height="14" viewBox="0 0 24 24"><rect x="6" y="2" width="12" height="20" rx="2" fill="#fff"/><rect x="8" y="4" width="8" height="13" fill="var(--lime)"/></svg></span>0400 555 217</div>
    </div>
    <div class="contact">
      <div><span class="icon"><svg width="14" height="14" viewBox="0 0 24 24"><rect x="2" y="5" width="20" height="14" rx="2" fill="#fff"/><path d="M3 6l9 7 9-7" stroke="var(--lime)" stroke-width="2" fill="none"/></svg></span>moira@tandemspeakworks.com</div>
      <div><span class="icon"><svg width="14" height="14" viewBox="0 0 24 24"><circle cx="12" cy="12" r="9" fill="none" stroke="#fff" stroke-width="2"/><path d="M3 12h18M12 3c3 3 3 15 0 18M12 3c-3 3-3 15 0 18" stroke="#fff" stroke-width="1.6" fill="none"/></svg></span>www.tandemspeakworks.com</div>
    </div>
  </div>
</div>
</body>
</html>
```